Evergreen Post-Service Drip Postcard Campaign (6-piece automated sequence)

Project: 6-Piece Evergreen Post-Service Postcard Drip Campaign
Size: 6 × 9 inches, full-color both sides, glossy UV coating - Back of card, right HALF needs to remain blank for printer. Please keep all fonts, designs and images within a safe zone.
Quantity: 6 unique designs (print-ready PDFs + editable source files)
Deadline: 10 business days
Creative Freedom
Pull colors, fonts, photos, and overall style directly from www.varnellpipeworks.example.
Tone: Clean, professional, trustworthy, helpful – never pushy.
Make each card visually striking and impossible to toss – you have plenty of room on 6 × 9, so go bold and beautiful while keeping the messaging clear.
Global Elements on Every Card
* Varnell Plumbing, Inc. logo
* Tagline: “Steady Hands, Fair Prices”
* Phone number: (555) 318-4270 (make it big and obvious)
* Footer line: “Serving Healdsburg • Santa Rosa • Petaluma • Windsor • Sebastopol • Rohnert Park • Sonoma County”
* QR codes where noted (we’ll supply the exact links)
Card-by-Card Content (exact wording – feel free to lay out creatively)
Card 1 – Thank You + Review Request
Front
“Thank You for Choosing Varnell Plumbing!”
“Your feedback helps neighbors across Sonoma County”
Back
“A 30-second review means the world to us”
We truly appreciate your business. A quick Raterly or Vouchy review helps neighbors in Sonoma County find honest plumbing when they need it most.
We proudly offer:
• Trenchless sewer repair (CIPP & pipe bursting)
• Water heater installation & repair
• Drain cleaning & camera inspections
• Leak detection
• Toilet, faucet & remodel work
• Sewer lateral video inspections
CTA: Scan QR → leave a quick Raterly or Vouchy review
Card 2 – 5 Warning Signs
Front
“5 Warning Signs Your Plumbing Is Trying to Tell You Something”
Back
“Catch these early – save thousands”
Keep this card on your fridge:
• Gurgling or bubbling drains
• Popping / banging water heater
• Rattling or banging pipes
• Discoloration or dampness around toilet base
• Dripping faucets that won’t stop
See any of these? We fix them fast, honestly, and with minimal mess.
CTA: Text WARNING to (555) 318-4270 → get your free troubleshooting guide
Card 3 – $99 Drain Refresh
Front
“$99 Professional Drain Refresh”
“Includes camera inspection from approved access point”
Back
Full drain cleaning + camera inspection from an approved exterior access point.
No digging · No mess · No surprises
Prevent backups before they happen.
CTA: Text DRAIN99 to (555) 318-4270 → book your $99 service
Card 4 – Referral $50
Front
“Refer a Neighbor – Both Save $50”
“Unlimited referrals – the more you send, the more you save”
Back
Know someone with plumbing headaches?
Refer anyone in Sonoma County and you both get $50 off your next service. No limits. One use per visit.
CTA: Text REFER + their name to (555) 318-4270 → $50 credit for both
Card 5 – 65-Point Inspection $149
Front
“65-Point Whole-House Plumbing Inspection – Only $149”
“Catch small problems before they become big bills”
Back
Average customer avoids $800+ in emergency repairs
Our technician performs a complete 65-point inspection covering water heater, pressure, drains, sewer lateral, fixtures, and more.
CTA: Text 65POINT to (555) 318-4270 → book your $149 inspection
Card 6 – Priority Service Card
Front
“Priority Service Card – Keep This!”
“You’re a Varnell Plumbing Priority Customer”
Back
As our valued returning customer you always get:
• We know you by name – no explaining your history twice
• We remember your home – past jobs, equipment, quirks
• We take great care of you – same honest pricing, same thorough work
• We’ll always make room when you really need us
Just mention you’re a returning customer when you call – we’ve got your back.
Call (555) 318-4270
Steady Hands, Fair Prices
Deliverables
• 6 print-ready 6 × 9 PDFs (300 dpi, CMYK, bleed)
• Editable source files
• All QR codes generated and tested (we’ll provide the exact URLs)
• One-page style guide summarizing colors/fonts from the website
Vouchy: https://www.vouchy.example/biz/varnell-plumbing-santa-rosa-2
Raterly: https://raterly.example/r/QX8KTmPbn-W4ZDR/review

```html
<!DOCTYPE html>
<html lang="en">
<head>
<meta charset="utf-8">
<title>Varnell Plumbing – 65-Point Inspection Postcard</title>
<link href="https://fonts.googleapis.com/css2?family=Krona+One&family=Poppins:wght@400;500;600&display=swap" rel="stylesheet">
<style>
  :root {
    --navy: #26398f;
    --navy-deep: #1f2c73;
    --sky: #1f88d6;
    --sun: #ecd41c;
    --tag-blue: #2a8fd7;
    --ink: #1b2350;
    --white: #ffffff;
    --stage: #5e5e5e;
    --rule: #8a8a8a;
  }
  * { margin: 0; padding: 0; box-sizing: border-box; }
  html, body { width: 1200px; height: 749px; overflow: hidden; }
  body { background: var(--stage); position: relative; font-family: "Poppins", sans-serif; }

  .postcard {
    position: absolute; top: 182px; width: 576px; height: 384px;
    background: var(--white); overflow: hidden;
    box-shadow: 0 4px 14px rgba(0,0,0,.35);
  }
  .postcard--front { left: 16px; }
  .postcard--back { left: 608px; }
  .layer { position: absolute; inset: 0; }

  /* Front */
  .brand-name {
    position: absolute; left: 24px; top: 40px; width: 200px;
    font-family: "Krona One", sans-serif; font-size: 15px; line-height: 21px;
    color: var(--ink); text-align: center;
  }
  .tagline-box {
    position: absolute; left: 294px; top: 25px; width: 188px; height: 38px;
    background: rgba(255,255,255,.85); padding: 3px 0 0 10px;
  }
  .tagline {
    font-family: "Krona One", sans-serif; font-size: 11.5px; line-height: 16px;
    color: var(--tag-blue);
  }
  .headline {
    position: absolute; left: 25px; top: 179px;
    font-family: "Krona One", sans-serif; font-size: 20.5px; line-height: 34px;
    color: var(--white); white-space: nowrap;
  }
  .headline .price { color: var(--sun); }
  .subline {
    position: absolute; left: 33px; top: 286px; padding-left: 9px;
    border-left: 1.5px solid var(--sun);
    font-size: 14.5px; line-height: 18px; color: var(--white);
  }
  .service-area {
    position: absolute; left: 0; top: 345px; width: 576px; height: 22px;
    background: rgba(31,40,110,.88); color: var(--white);
    font-size: 10.6px; line-height: 22px; padding-left: 21px; white-space: nowrap;
  }

  /* Back */
  .back-headline {
    position: absolute; left: 25px; top: 36px;
    font-family: "Krona One", sans-serif; font-size: 15.5px; line-height: 24px;
    color: var(--white);
  }
  .back-headline .figure { color: var(--sun); }
  .back-body {
    position: absolute; left: 25px; top: 148px; width: 200px; padding-left: 9px;
    border-left: 1.5px solid var(--sun);
    font-size: 13.5px; line-height: 17px; color: var(--white);
  }
  .cta-text { position: absolute; left: 25px; top: 262px; font-size: 13.5px; color: var(--white); }
  .cta-phone {
    position: absolute; left: 25px; top: 281px;
    font-family: "Krona One", sans-serif; font-size: 14px; color: var(--sun);
  }
  .cta-book { position: absolute; left: 25px; top: 313px; font-size: 13.5px; color: var(--white); }
  .cta-price {
    position: absolute; left: 25px; top: 331px; font-size: 13.5px; color: var(--white);
  }
  .cta-price strong { font-size: 22px; font-weight: 600; color: var(--sun); }
  .stamp-box {
    position: absolute; left: 487px; top: 59px; width: 60px; height: 60px;
    border: 1px solid var(--rule);
  }
  .address-line {
    position: absolute; left: 342px; width: 194px; height: 0;
    border-top: 1px solid var(--rule);
  }
</style>
</head>
<body>

<section class="postcard postcard--front">
  <svg class="layer" viewBox="0 0 576 384" width="576" height="384">
    <defs>
      <linearGradient id="trenchTones" x1="0" y1="0" x2="1" y2="0">
        <stop offset="0" stop-color="#ffffff" stop-opacity="0"/>
        <stop offset=".3" stop-color="#c9b4a0"/>
        <stop offset=".6" stop-color="#9fb7c4"/>
        <stop offset="1" stop-color="#8d6446"/>
      </linearGradient>
      <linearGradient id="navyFill" x1="0" y1="0" x2="1" y2="1">
        <stop offset="0" stop-color="#2b43a0"/>
        <stop offset="1" stop-color="#1f2c73"/>
      </linearGradient>
      <linearGradient id="heaterTones" x1="0" y1="0" x2="1" y2="1">
        <stop offset="0" stop-color="#f1efeb"/>
        <stop offset=".6" stop-color="#d9d3cb"/>
        <stop offset="1" stop-color="#a88c70"/>
      </linearGradient>
      <clipPath id="heaterClip"><circle cx="447" cy="357" r="100"/></clipPath>
    </defs>
    <rect x="250" y="0" width="326" height="200" fill="url(#trenchTones)" role="img" aria-label="Photo of a trench with newly lined sewer pipe and utility lines"/>
    <path d="M290,172 C400,205 500,165 576,82 L576,384 L290,384 Z" fill="var(--sun)"/>
    <path d="M0,133 C110,100 220,118 320,165 C420,210 500,200 576,158 L576,384 L0,384 Z" fill="var(--sky)"/>
    <path d="M0,150 C110,118 220,135 320,180 C420,222 500,212 576,172 L576,384 L0,384 Z" fill="url(#navyFill)"/>
    <circle cx="447" cy="357" r="112" fill="var(--sun)"/>
    <rect x="347" y="257" width="200" height="200" fill="url(#heaterTones)" clip-path="url(#heaterClip)" role="img" aria-label="Photo of wall-mounted tankless water heaters with copper piping"/>
  </svg>
  <div class="brand-name">VARNELL<br>PLUMBING, INC.</div>
  <div class="tagline-box"><p class="tagline">Steady Hands,<br>Fair Prices</p></div>
  <h1 class="headline">65-Point Whole-House<br>Plumbing Inspection –<br><span class="price">Only $149</span></h1>
  <p class="subline">Catch small problems before they<br>become big bills</p>
  <p class="service-area">Serving Healdsburg • Santa Rosa • Petaluma • Windsor • Sebastopol • Rohnert Park • Sonoma County</p>
</section>

<section class="postcard postcard--back">
  <svg class="layer" viewBox="0 0 576 384" width="576" height="384">
    <defs>
      <linearGradient id="backNavy" x1="0" y1="0" x2="1" y2="1">
        <stop offset="0" stop-color="#233896"/>
        <stop offset="1" stop-color="#2a47a6"/>
      </linearGradient>
    </defs>
    <path d="M0,0 H264 C306,60 302,140 287,200 C270,270 262,330 308,384 H0 Z" fill="var(--sun)"/>
    <path d="M0,0 H252 C292,60 288,140 272,200 C255,270 245,330 282,384 H0 Z" fill="var(--sky)"/>
    <path d="M0,0 H240 C278,60 275,140 260,200 C243,270 232,330 262,384 H0 Z" fill="url(#backNavy)"/>
  </svg>
  <h2 class="back-headline">Average customer<br>avoids <span class="figure">$800+</span><br>in emergency<br>repairs</h2>
  <p class="back-body">Our technician performs a complete 65-point inspection covering water heater, pressure, drains, sewer lateral, fixtures, and more.</p>
  <p class="cta-text">Text 65POINT to</p>
  <p class="cta-phone">(555) 318-4270</p>
  <p class="cta-book">Book your</p>
  <p class="cta-price"><strong>$149</strong> inspection</p>
  <div class="stamp-box"></div>
  <div class="address-line" style="top:186px"></div>
  <div class="address-line" style="top:208px"></div>
  <div class="address-line" style="top:230px"></div>
  <div class="address-line" style="top:252px"></div>
  <div class="address-line" style="top:274px"></div>
</section>

</body>
</html>
```